New Stationary for our business

We are a gift business and would like to create a new corporate image with new stationary and design.

We would like a Classic Corporate look with a touch of Flair.

We would need:
Envelopes
Letter Head
Business Cards
With Comp Slips
Note Pads
Etc...

Our details are:

Basket Haven Pty Ltd
518 Pelling Street, Carrow Vale, Victoria, 3071
1800 742 918
www.baskethaven.com.au
sales@baskethaven.com.au

ABN: 62 804 319 775

Target Market(s)

Corporate Look

Industry/Entity Type

Marketing

Contact Information for Business Card

Basket Haven Pty Ltd
1800 742 918
518 Pelling Street
Carrow Vale 3071
Victoria Australia

Darren Pelloni - Managing Director
darren.pelloni@baskethaven.com.au
0417 586 902

Logo Text

Basket Haven - The Present Experts

Colors

Designer to choose colors to be used in the design.

Requirements
Must have
• Look and Feel upmarket and exclusive

```html
<!DOCTYPE html>
<html lang="en">
<head>
<meta charset="utf-8">
<title>Basket Haven — Business Card</title>
<link rel="stylesheet" href="https://fonts.googleapis.com/css2?family=Montserrat:wght@400;500;600;700&display=swap">
<style>
  :root {
    --teal: #40d0c6;
    --white: #ffffff;
    --ink: #55585c;
    --ink-soft: #6b6e72;
    --mark-grey: #a3a3a3;
    --backdrop: #eceeef;
  }
  * { margin: 0; padding: 0; box-sizing: border-box; }
  html, body {
    width: 1200px;
    height: 880px;
    overflow: hidden;
    background: var(--backdrop);
    font-family: "Montserrat", sans-serif;
  }
  .canvas { position: relative; width: 1200px; height: 880px; }

  .card {
    position: absolute;
    width: 560px;
    height: 340px;
    border-radius: 22px;
    box-shadow: 0 14px 30px rgba(0, 0, 0, 0.12);
  }

  /* Front */
  .card-front {
    left: 70px;
    top: 70px;
    background: var(--teal);
  }
  .brand {
    position: absolute;
    display: flex;
    align-items: center;
    gap: 14px;
    font-weight: 600;
    letter-spacing: 0.5px;
  }
  .brand-square {
    width: 34px;
    height: 34px;
    background: var(--mark-grey);
  }
  .card-front .brand {
    left: 0;
    right: 0;
    top: 128px;
    justify-content: center;
    color: var(--white);
    font-size: 40px;
  }
  .front-web {
    position: absolute;
    left: 0;
    right: 0;
    bottom: 52px;
    text-align: center;
    color: var(--white);
    font-size: 13px;
    font-weight: 600;
    letter-spacing: 0.3px;
  }

  /* Back */
  .card-back {
    left: 570px;
    top: 470px;
    background: var(--white);
  }
  .card-back .brand {
    left: 44px;
    top: 52px;
    color: var(--teal);
    font-size: 30px;
  }
  .card-back .brand-square { width: 30px; height: 30px; }

  .person {
    position: absolute;
    left: 44px;
    bottom: 58px;
    color: var(--ink);
  }
  .person-name { font-size: 19px; font-weight: 700; }
  .person-role { font-size: 12.5px; font-weight: 500; color: var(--ink-soft); margin-top: 3px; }

  .contact {
    position: absolute;
    left: 310px;
    bottom: 46px;
    color: var(--ink);
    font-size: 11.5px;
    line-height: 1.45;
    font-weight: 500;
  }
  .contact-address { margin-bottom: 14px; }
  .contact-lines {
    border-left: 3px solid var(--teal);
    padding-left: 10px;
  }
</style>
</head>
<body>
<main class="canvas">
  <section class="card card-front" aria-label="Business card front">
    <div class="brand"><span class="brand-square"></span><span class="brand-name">Basket Haven</span></div>
    <p class="front-web">www.baskethaven.com.au</p>
  </section>

  <section class="card card-back" aria-label="Business card back">
    <div class="brand"><span class="brand-square"></span><span class="brand-name">Basket Haven</span></div>
    <div class="person">
      <p class="person-name">Marla Pentridge</p>
      <p class="person-role">Managing Partner</p>
    </div>
    <div class="contact">
      <p class="contact-address">518 Pelling Street,<br>Carrow Vale, Victoria, 3071</p>
      <div class="contact-lines">
        <p>1800 742 918</p>
        <p>www.baskethaven.com.au</p>
        <p>sales@baskethaven.com.au</p>
      </div>
    </div>
  </section>
</main>
</body>
</html>
```